Product flyer with pricing

We manufacture iconic and luxury vending trailers. for our first trailer we need a flyer created to give to prospective clients with base pricing. I am uploading an example along with graphic files.

```html
<!DOCTYPE html>
<html lang="en">
<head>
<meta charset="utf-8">
<title>Rustic Barn Loft Mini – Luxury Mobile Vending House</title>
<link rel="stylesheet" href="https://fonts.googleapis.com/css2?family=Oswald:wght@600;700&family=Arimo:wght@400;700&display=swap">
<style>
  :root{
    --green:#6ab04c;
    --green-dark:#5e9f43;
    --orange:#e39c2b;
    --black:#0d0d0d;
    --grey:#c9c9c9;
    --ink:#1a1a1a;
    --white:#ffffff;
    --canvas:#dde6ef;
    --photo-a:#b9c6d3;
    --photo-b:#e9ecef;
  }
  *{margin:0;padding:0;box-sizing:border-box}
  html,body{width:1200px;height:1200px;overflow:hidden;background:var(--canvas)}
  .flyer{
    position:absolute;left:190px;top:20px;width:912px;height:1290px;
    background:var(--white);transform:scale(.9);transform-origin:0 0;
    font-family:"Arimo",Arial,sans-serif;color:var(--ink);overflow:hidden;
  }
  .flyer-shapes{position:absolute;inset:0}
  .title{position:absolute;left:46px;font-family:"Oswald","Arial Narrow",sans-serif;font-weight:700;font-size:44px;line-height:1;text-transform:uppercase;letter-spacing:.5px;white-space:nowrap}
  .title-line{display:block;height:52px}
  .title--lead{top:38px;color:var(--white)}
  .title--sub{top:145px;color:var(--ink)}
  .brand{position:absolute;left:690px;top:70px;display:flex;align-items:center;gap:10px;font-family:"Arimo",Arial,sans-serif;font-weight:700;font-size:22px;line-height:1.1;color:var(--orange)}
  .brand-dot{width:22px;height:22px;border-radius:50%;background:var(--green)}
  .price{position:absolute;left:46px;top:426px;font-family:"Oswald","Arial Narrow",sans-serif;font-weight:700;font-size:44px;color:var(--white);letter-spacing:.5px}
  .pill{position:absolute;height:40px;background:var(--green);color:var(--white);font-size:31px;line-height:40px;text-align:center;border-radius:4px;box-shadow:0 6px 5px -2px rgba(0,0,0,.35)}
  .pill--features{left:43px;top:546px;width:326px}
  .pill--options{left:501px;top:618px;width:326px}
  .pill--uses{left:293px;top:934px;width:327px}
  .list{position:absolute;list-style:none;font-size:19px;line-height:24px}
  .list li{position:relative;padding-left:14px}
  .list li::before{content:"";position:absolute;left:0;top:9px;width:8px;height:8px;border-radius:50%;background:var(--orange)}
  .list--features{left:46px;top:615px;width:395px}
  .list--options{left:501px;top:676px;width:360px}
  .cost{color:var(--green);font-weight:700}
  .uses-band{position:absolute;left:0;top:1002px;width:912px;height:42px;background:var(--orange)}
  .use{position:absolute;top:1009px}
  .use-head{font-size:24px;font-weight:700;color:var(--white);height:48px}
  .use-body{font-size:19px;line-height:24px;width:180px}
  .use--food{left:56px}
  .use--retail{left:278px}
  .use--corporate{left:497px}
  .use--fund{left:711px}
  .use--fund .use-body{width:160px}
  .web{position:absolute;left:54px;top:1240px;font-size:31px;font-weight:700;color:var(--white)}
  .phone{position:absolute;left:586px;top:1210px;font-family:"Oswald","Arial Narrow",sans-serif;font-weight:700;font-size:44px;color:var(--white);letter-spacing:1px}
</style>
</head>
<body>
<main class="flyer">
  <svg class="flyer-shapes" width="912" height="1290" viewBox="0 0 912 1290">
    <defs>
      <linearGradient id="photoTone" x1="0" y1="0" x2="0" y2="1">
        <stop offset="0" stop-color="var(--photo-a)"/>
        <stop offset=".55" stop-color="var(--photo-b)"/>
        <stop offset="1" stop-color="#6d6f73"/>
      </linearGradient>
    </defs>
    <polygon points="478,0 538,0 688,146 912,146 912,582 653,582 473,399 0,399 0,324 440,324" fill="var(--orange)"/>
    <polygon points="0,0 478,0 612,146 436,324 0,324" fill="var(--green)"/>
    <polygon points="0,36 500,36 560,142 0,142" fill="var(--green-dark)"/>
    <polygon points="626,162 912,162 912,542 613,542 460,330" fill="url(#photoTone)" role="img" aria-label="Photo of the white board-and-batten vending trailer with serving window and tandem wheels"/>
    <g stroke="var(--white)" stroke-width="3" fill="url(#photoTone)">
      <polygon points="58,268 124,268 157,326 124,384 58,384 25,326" role="img" aria-label="Front view of the vending house"/>
      <polygon points="205,268 271,268 304,326 271,384 205,384 172,326" role="img" aria-label="Side view of the vending house on its trailer"/>
      <polygon points="351,268 417,268 450,326 417,384 351,384 318,326" role="img" aria-label="Rear angle of the vending house"/>
    </g>
    <polygon points="0,419 462,419 525,482 0,482" fill="var(--black)"/>
    <polygon points="0,484 520,484 526,499 0,499" fill="var(--grey)"/>
    <polygon points="0,1227 428,1227 368,1290 0,1290" fill="var(--black)"/>
    <polygon points="398,1290 498,1191 912,1191 912,1290" fill="var(--orange)"/>
    <polygon points="488,1290 588,1199 912,1199 912,1290" fill="var(--green)"/>
  </svg>

  <h1 class="title title--lead"><span class="title-line">The</span><span class="title-line">“Rustic Barn Loft Mini”</span></h1>
  <h2 class="title title--sub"><span class="title-line">Luxury</span><span class="title-line">Mobile Vending House</span></h2>

  <div class="brand"><span class="brand-dot"></span><span>Little Sunroof<br>Builds</span></div>

  <p class="price">BASE PRICE: $45,000</p>

  <h3 class="pill pill--features">Base unit features:</h3>
  <ul class="list list--features">
    <li>Trailer features tandem wheels w/ brakes</li>
    <li>Steel frame construction for fire<br>Retardation safety and weight reduction.</li>
    <li>100% off grid with solar and lithium<br>battery system allowing the trailer to be used in places not accessible by traditional trailers.</li>
    <li>80 gallon water supply tank</li>
    <li>100 gallon waste water tank</li>
    <li>Cupboards, cabinets &amp; four stainless steel sinks.</li>
    <li>60” Gas shock serving window</li>
  </ul>

  <h3 class="pill pill--options">Available options:</h3>
  <ul class="list list--options">
    <li>HVAC - Kelvar Mini Split - <span class="cost">$1,800</span></li>
    <li>Cooler / Glass front Commercial refrig-erator - <span class="cost">$1,600</span></li>
    <li>Upper loft storage area - <span class="cost">$1,200</span></li>
    <li>Signage and graphics - <span class="cost">$2,000 - $5,000</span> depend on complexity</li>
    <li>Ice machine - <span class="cost">$1,100</span></li>
    <li>Other custom items available on<br>request.</li>
  </ul>

  <h3 class="pill pill--uses">Use cases:</h3>
  <div class="uses-band"></div>
  <section class="use use--food"><h4 class="use-head">Food:</h4><p class="use-body">Lemonade, Coffee, pizza<br>cookies, dough-<br>nuts, barbecue and more!</p></section>
  <section class="use use--retail"><h4 class="use-head">Retail:</h4><p class="use-body">Clothing, watches, jewelry, flowers and more!</p></section>
  <section class="use use--corporate"><h4 class="use-head">Corporate:</h4><p class="use-body">Product info, demonstration, information, brand awareness.</p></section>
  <section class="use use--fund"><h4 class="use-head">Fundraisers:</h4><p class="use-body">Girls/boy sports,<br>non profits, etc.</p></section>

  <p class="web">www.littlesunroof.com</p>
  <p class="phone">123-456-7890</p>
</main>
</body>
</html>
```